New therapy private practice needs a 2 sided postcard announcing location and services

We need a postcard sized card that is TWO SIDED and shares our new location and services offered. (new location is 3842. W. 58th #2300 in Tulsa, OK 74152) Name of the therapy business is "Bright Path! Counseling". Services offered include individual, marriage, family and group counseling. My phone number to place on the card is (918) 555-0143 and someone can call to schedule a free 20 minute consultation at that number.

These cards will also be mailed in an enclosed envelope or placed in welcome baskets as a marketing tool with possible referral sources like churches, doctors, and lawyers. (That means there does not have to be a space for an address or stamp to mail to. Full use of both sides of the card is important) We would like to see designs that use softer colors such as blue, purples, or greens. The final design should communicate a feeling of peace and hope and a sense of freshness and approachability. Incorporating a tag line such as..... "where you'll find hope!" would be good. My website is www.brightpathnow.example and extra info about my practice is on there. It is important my credentials are listed on the postcard. Lena Marsh Voight, LPC-S, LMFT

I am not looking for a bunch of "box looking pictures". The pictures I am uploading are for ideas, although my logo and picture should be used. I like the type of picture I have on my homepage of my website with the quote "Let your hopes, not your fears shape your future"

Target Market(s)

Primarily women and couples looking for counseling for relationships, anxiety, depression, or life transitions.

Font styles to use
Serif
Script

Colors
3276b5
85acd3
86cfc6
33b8a4
cadf82
876aae
9bcb3c

Requirements
Must have
• My picture, address, website, and phone number as well as my logo.
• Address is: 3842 W. 58th Street #2300 Tulsa, OK 74152
• Web: www.brightpathnow.example
• Email: lena@brightpathnow.example
• Phone: (918) 555-0143
• "Hope anchors the soul" - Heb. 6:19
• On my website, I have a 2 minute video of myself. This may be helpful to watch in getting a "feel" for my counseling practice.
• Services Provided: ANXIETY | DEPRESSION | LIFE TRANSITIONS | MARRIAGE COUNSELING | SEPARATION AND DIVORCE | WOMEN’S ISSUES | ADDICTIONS AND INFIDELITY | PARENT/CHILD RELATIONSHIPS | FAMILY CONFLICT | TRAUMA/GRIEF AND LOSS
Nice to have
• A combination of print and script would be nice. A feeling of tranquility and hope
• I would like to have the statement at the bottom of the card.... " It is my desire for you to discover that no matter the situation you are currently going through….. there’s hope!"
• It would also be nice to have a small area that says: Lena is a graduate of Western Calloway College and has been in private practice for 11 years. She is a regular monthly co-host on the Meadow Broadcast Group at 97.3 FM
Should not have
• Heavy bold or abrasive feel

```html
<!DOCTYPE html>
<html lang="en">
<head>
<meta charset="utf-8">
<title>Bright Path! Counseling – Postcard</title>
<link href="https://fonts.googleapis.com/css2?family=Montserrat:wght@300;400;600;700;800&family=Raleway:wght@300;400;500;700&display=swap" rel="stylesheet">
<style>
:root{
  --board-light:#f7f7f7;
  --board-dark:#dcdcdc;
  --card:#ffffff;
  --card-tint:#f3f3f3;
  --green:#5b9f4c;
  --green-soft:#6aad80;
  --green-line:#4f9a55;
  --purple:#3d2a7c;
  --purple-soft:#4a3a8c;
  --blue:#3b6d9c;
  --ink:#222222;
  --grey-label:#333333;
}
*{box-sizing:border-box;margin:0;padding:0}
html,body{width:822px;height:1200px;overflow:hidden}
body{
  background:radial-gradient(ellipse at 50% 45%,var(--board-light) 0%,var(--board-dark) 100%);
  font-family:"Raleway",sans-serif;color:var(--ink);position:relative;
}
.card{position:absolute;left:62px;width:672px;height:521px;background:var(--card);
  box-shadow:0 3px 10px rgba(0,0,0,.18);overflow:hidden}
.card--front{top:41px}
.card--back{top:620px;height:522px}
.side-label{position:absolute;left:767px;font-family:"Raleway",sans-serif;font-weight:300;
  font-size:30px;color:var(--grey-label);letter-spacing:1px;transform:rotate(-90deg);transform-origin:left top}
.side-label--front{top:560px}
.side-label--back{top:1140px}

/* front */
.hero-photo{position:absolute;left:0;top:0;width:672px;height:303px;
  background:linear-gradient(160deg,#3a3a2e 0%,#2b2d22 35%,#4a4030 60%,#1c1a14 100%)}
.headline-frame{position:absolute;left:24px;top:37px;width:314px;height:246px;border:1px solid rgba(255,255,255,.85)}
.headline{position:absolute;left:44px;top:48px;color:#fff;font-family:"Montserrat",sans-serif;line-height:46px}
.headline .strong{font-weight:800;font-size:45px;display:block;letter-spacing:-.5px}
.headline .light{font-weight:300;font-size:40px;display:block}
.front-lower{position:absolute;left:0;top:303px;width:672px;height:218px;
  background:linear-gradient(135deg,var(--card) 0%,var(--card-tint) 50%,var(--card) 100%)}
.brand{position:absolute;display:flex;align-items:center;gap:10px;color:var(--green);
  font-family:"Raleway",sans-serif;font-weight:500}
.brand__dot{border-radius:50%;background:var(--green);flex:none}
.brand--front{left:30px;top:370px;font-size:30px;line-height:34px}
.brand--front .brand__dot{width:40px;height:40px}
.front-web{position:absolute;left:39px;top:490px;font-size:13px;letter-spacing:3.4px;color:var(--ink)}
.hope-box{position:absolute;left:340px;top:285px;width:316px;height:220px;border:1px solid var(--green-line);
  text-align:center;padding:28px 16px 0}
.hope-box__title{font-family:"Montserrat",sans-serif;font-size:24px;color:var(--purple);font-weight:700;letter-spacing:-.3px}
.hope-box__title .thin{font-weight:400}
.hope-box__title .accent{color:var(--green)}
.hope-box__text{font-size:13px;line-height:18px;margin-top:14px;color:var(--ink)}
.hope-box__rule{width:58px;height:1px;background:var(--green);margin:14px auto 18px}
.hope-box__radio{font-size:12px;line-height:16px;color:var(--purple-soft)}

/* back */
.portrait{position:absolute;left:0;top:0;width:206px;height:282px;
  background:linear-gradient(150deg,#c98a2e 0%,#a86a25 40%,#5a2a38 75%,#2d2c3a 100%)}
.bio{position:absolute;left:191px;top:18px;width:465px;height:250px;background:var(--card);
  border:1px solid var(--green-soft);padding:12px 18px 0 40px;text-align:center}
.bio__title{font-family:"Raleway",sans-serif;font-weight:400;font-size:26px;color:var(--ink)}
.bio__title .name{font-family:"Montserrat",sans-serif;font-weight:700;color:var(--green-soft)}
.bio__rule{width:60px;height:1px;background:var(--green-soft);margin:4px auto 10px}
.bio__text{font-size:12.4px;line-height:17.2px;text-align:justify;text-align-last:center;color:var(--ink)}
.services{font-family:"Montserrat",sans-serif;font-weight:700;font-size:12.6px;line-height:18px;color:var(--blue);
  margin-top:10px;text-align:justify;text-align-last:center}
.back-lower{position:absolute;left:0;top:282px;width:672px;height:124px;
  background:linear-gradient(135deg,var(--card) 0%,var(--card-tint) 60%,var(--card) 100%)}
.brand--back{left:22px;top:310px;font-size:21px;line-height:24px}
.brand--back .brand__dot{width:28px;height:28px}
.room{position:absolute;top:278px;height:118px}
.room--1{left:224px;width:90px;background:linear-gradient(170deg,#8a7a66,#5b4a3c 60%,#9c9488)}
.room--2{left:321px;width:174px;background:linear-gradient(170deg,#8f8473,#b5ab9c 55%,#7a6f62)}
.room--3{left:501px;width:156px;background:linear-gradient(170deg,#c9c4bc,#a9a49c 55%,#8d8a84)}
.cta-rule{position:absolute;left:0;top:405px;width:672px;height:4px;background:var(--green-soft)}
.cta{position:absolute;left:0;top:412px;width:672px;text-align:center;font-size:17px;color:var(--ink)}
.cta strong{font-family:"Montserrat",sans-serif;font-weight:700;color:var(--green);font-size:17px}
.contact-band{position:absolute;left:0;top:434px;width:672px;height:88px;background:var(--green-soft);
  color:#fff;text-align:center}
.contact-band__phone{font-family:"Montserrat",sans-serif;font-weight:700;font-size:28px;margin-top:6px;
  display:flex;align-items:center;justify-content:center;gap:12px}
.contact-band__line{font-size:14.5px;margin-top:2px;display:flex;align-items:center;justify-content:center;gap:8px}
.contact-band__line .gap{width:14px}
.icon{fill:#fff;flex:none}
</style>
</head>
<body>

<section class="card card--front">
  <div class="hero-photo" role="img" aria-label="Photo of a woman sitting on a rock ledge overlooking a misty forested valley at sunset"></div>
  <div class="headline-frame"></div>
  <h1 class="headline">
    <span class="strong">Let your</span>
    <span class="strong">Hopes,</span>
    <span class="light">not your hurts,</span>
    <span class="light">shape your</span>
    <span class="light">future.</span>
  </h1>
  <div class="front-lower"></div>
  <div class="brand brand--front"><span class="brand__dot"></span><span>Bright Path!<br>Counseling</span></div>
  <div class="front-web">www.brightpathnow.example</div>
  <div class="hope-box">
    <h2 class="hope-box__title">Where you'll <span class="thin">find</span> <span class="accent">hope!</span></h2>
    <p class="hope-box__text">It is my desire for you to discover that no matter the situation you are currently going through..... there's hope!</p>
    <div class="hope-box__rule"></div>
    <p class="hope-box__radio">Lena can be heard monthly on the<br>Meadow Broadcast Group Radio Station at 97.3 FM</p>
  </div>
</section>
<div class="side-label side-label--front">FRONT</div>

<section class="card card--back">
  <div class="portrait" role="img" aria-label="Portrait photo of the counselor outdoors with autumn foliage behind her"></div>
  <div class="bio">
    <h2 class="bio__title">Hello! I am <span class="name">Lena Marsh Voight</span></h2>
    <div class="bio__rule"></div>
    <p class="bio__text">My focus was on clients and their families who struggled with mental health as well as chemical dependency issues. From there, I began working at a non-profit agency with families affected by trauma. In 2007, I began my private practice and have been privileged to work with adolescents, individuals, couples, families, and groups focusing on a range of issues including:</p>
    <p class="services">Anxiety | Depression | Life Transitions | Marriage Counseling | Separation And Divorce | Women’s Issues | Addictions And Infidelity | Parent/Child Relationships | Family Conflict | Trauma/Grief And Loss</p>
  </div>
  <div class="back-lower"></div>
  <div class="brand brand--back"><span class="brand__dot"></span><span>Bright Path!<br>Counseling</span></div>
  <div class="room room--1" role="img" aria-label="Office photo: two armchairs beside a lamp table"></div>
  <div class="room room--2" role="img" aria-label="Office photo: sofa with wall clock and artwork"></div>
  <div class="room room--3" role="img" aria-label="Office photo: seating area with sofas and coffee table"></div>
  <div class="cta-rule"></div>
  <p class="cta">call to schedule a <strong>FREE 20 MINUTE CONSULTATION</strong></p>
  <div class="contact-band">
    <div class="contact-band__phone">
      <svg class="icon" width="20" height="20" viewBox="0 0 20 20" aria-hidden="true"><circle cx="10" cy="10" r="10"/><path d="M7 5.5c-1.5 1-1.6 3.6 0 6.5s3.8 4 5.6 3.6l-.8-2.8-1.6.3c-.8-.6-1.6-2-1.8-3l1.4-.8L9 5.6z" fill="#6aad80"/></svg>
      <span>918 555 0143</span>
    </div>
    <div class="contact-band__line">
      <svg class="icon" width="12" height="14" viewBox="0 0 12 14" aria-hidden="true"><path d="M6 0a6 6 0 0 0-6 6c0 4 6 8 6 8s6-4 6-8a6 6 0 0 0-6-6zm0 8.3A2.3 2.3 0 1 1 6 3.7a2.3 2.3 0 0 1 0 4.6z"/></svg>
      <span>3842 W. 58th Street #2300 Tulsa, OK 74152</span>
    </div>
    <div class="contact-band__line">
      <svg class="icon" width="13" height="13" viewBox="0 0 13 13" aria-hidden="true"><circle cx="6.5" cy="6.5" r="6.5"/><path d="M1 6.5h11M6.5 1c2 2 2 9 0 11M6.5 1c-2 2-2 9 0 11" stroke="#6aad80" fill="none"/></svg>
      <span>www.brightpathnow.example</span>
      <span class="gap"></span>
      <svg class="icon" width="13" height="13" viewBox="0 0 13 13" aria-hidden="true"><circle cx="6.5" cy="6.5" r="6.5"/><path d="M3.5 4.5h6v4h-6zM3.5 4.5l3 2.2 3-2.2" stroke="#6aad80" fill="none" stroke-width=".9"/></svg>
      <span>lena@brightpathnow.example</span>
    </div>
  </div>
</section>
<div class="side-label side-label--back">BACK</div>

</body>
</html>
```